TV - business card

Tidewell Vantage is an insurance brokerage firm, inovative, proactive, vigorous, which aims to become the leader of the insurance brokers in Anfrica. We should like to get some designs which should be avoided also in Gray / Metallic for the Administration and Orange / Blue for the Managers (ike in the picture sent). The Blue / Green logo is not the correct one, but the source of the file. Please adjust the color accordingly for the business cards. 1 / Orange / Blue 2 / Gray / Metallic We want something classic but which is transmitted strenght, inovation, modernity and most of all, rapidity. We want something start-up like, very punchy and catching eye remaining profesional at the same time. Name: Delton Ashgrove Function: Managing Director Address: N ° 73/74 Cmt. Bolembe - R / C 2B Esquerda - Bairro Quimbuta - Luanda Tel: (+244) 947 385 619 Email: delton.ashgrove@tidewell-v.com Website: www.tidewell-v. com We want classic in the front and creative, colorfull at the back. The cards will be printed in relief, with very high quality of paper.
Industry/Entity Type
Insurance Broker
Colors
Designer to choose colors to be used in the design.
Look and feel

```html
<!DOCTYPE html>
<html lang="en">
<head>
<meta charset="utf-8">
<title>Tidewell Vantage – Business Card</title>
<link rel="stylesheet" href="https://fonts.googleapis.com/css2?family=Arimo:wght@400;700&display=swap">
<style>
  :root {
    --bg: #2b2b2b;
    --green: #0e9444;
    --orange: #e8731e;
    --orange-dark: #a9510f;
    --white: #ffffff;
    --paper: #f3f3f3;
    --ink: #1d1d1d;
  }
  * { box-sizing: border-box; margin: 0; padding: 0; }
  html, body {
    width: 1200px; height: 997px; overflow: hidden;
    background: var(--bg);
    font-family: "Arimo", Arial, sans-serif;
  }
  .card {
    position: absolute;
    width: 520px; height: 300px;
    border-radius: 22px;
    overflow: hidden;
    box-shadow: 0 14px 30px rgba(0,0,0,.45);
  }
  /* Front */
  .card--front {
    left: 80px; top: 170px;
    background: var(--green);
    display: flex; align-items: center; justify-content: center; gap: 16px;
  }
  .brand-dot {
    width: 54px; height: 54px; border-radius: 50%;
    background: var(--orange);
    flex: none;
  }
  .brand-name {
    font-weight: 700; font-size: 38px; letter-spacing: 1px;
    color: var(--white); text-transform: uppercase;
  }
  /* Back */
  .card--back {
    left: 600px; top: 500px;
    background: var(--paper);
  }
  .card--back .shapes { position: absolute; inset: 0; }
  .back-brand {
    position: absolute; top: 50px; left: 0; right: 0;
    display: flex; align-items: center; justify-content: center; gap: 12px;
  }
  .back-brand .brand-dot { width: 40px; height: 40px; }
  .back-brand .brand-name { color: var(--green); font-size: 28px; }
  .holder {
    position: absolute; left: 100px; top: 145px; width: 250px;
    text-align: center; color: var(--white);
  }
  .holder__name { font-weight: 700; font-size: 16px; letter-spacing: .5px; text-transform: uppercase; line-height: 18px; }
  .holder__role { font-size: 13px; line-height: 16px; margin-top: 1px; }
  .company {
    position: absolute; right: 24px; top: 202px;
    text-align: right; color: var(--ink); font-size: 10.5px; line-height: 1.4;
    font-style: normal;
  }
  .company__name { font-weight: 700; font-size: 11.5px; }
  .contacts {
    position: absolute; left: 26px; bottom: 20px;
    list-style: none; color: var(--white); font-size: 13px;
  }
  .contacts li { display: flex; align-items: center; gap: 10px; line-height: 22px; }
  .contacts svg { width: 13px; height: 13px; fill: var(--white); flex: none; }
</style>
</head>
<body>

<section class="card card--front" aria-label="Card front">
  <span class="brand-dot"></span>
  <span class="brand-name">Tidewell Vantage</span>
</section>

<section class="card card--back" aria-label="Card back">
  <svg class="shapes" viewBox="0 0 520 300" width="520" height="300" aria-hidden="true">
    <rect x="0" y="180" width="520" height="120" fill="var(--green)"/>
    <rect x="0" y="176" width="520" height="4" fill="var(--orange)"/>
    <polygon points="60,180 88,194 110,180" fill="var(--orange-dark)"/>
    <polygon points="340,180 362,194 390,180" fill="var(--orange-dark)"/>
    <polygon points="60,180 100,138 350,138 390,180 362,194 88,194" fill="var(--orange)"/>
  </svg>

  <div class="back-brand">
    <span class="brand-dot"></span>
    <span class="brand-name">Tidewell Vantage</span>
  </div>

  <div class="holder">
    <p class="holder__name">Delton Ashgrove</p>
    <p class="holder__role">Managing Director</p>
  </div>

  <address class="company">
    <p class="company__name">Tidewell Vantage Pvt Ltd</p>
    <p>N ° 73/74 Cmt. Bolembe - R / C 2B Esquerda</p>
    <p>Bairro Quimbuta - Luanda</p>
  </address>

  <ul class="contacts">
    <li>
      <svg viewBox="0 0 16 16"><path d="M3 1h3l1.5 4-2 1.3a9 9 0 0 0 4.2 4.2L11 8.5l4 1.5v3a2 2 0 0 1-2 2A13 13 0 0 1 1 3a2 2 0 0 1 2-2z"/></svg>
      (+244) 947 385 619
    </li>
    <li>
      <svg viewBox="0 0 16 16"><path d="M1 3h14v10H1zM2 4.5v.4l6 4 6-4v-.4z"/></svg>
      delton.ashgrove@tidewell-v.com
    </li>
    <li>
      <svg viewBox="0 0 16 16"><path d="M8 1l7 6.5h-2V15H9.5v-4h-3v4H3V7.5H1z"/></svg>
      www.tidewell-v. com
    </li>
  </ul>
</section>

</body>
</html>
```